University of Carrowind Larkmoor Saxophone Quartet Concert

We need a poster design advertising the Larkmoor Saxophone Quartet Concert on Tuesday, April 23 at 5pm. The program concert will consist of 2 works by Peter Oskivar: Harbor Lanterns and Vesper ledger. These two works should be included on the poster being the concert is featuring the composer and his works. Peter Oskivar is known for his very "natural" sounding music. He resides in Montana and writes mostly from his small cottage in the mountains. This same idea of nature and "Montana" should be included on the poster design. He is deeply influenced by Telvane and most of the music he writes is play offs from Telvane Chorales.

The concert title is: "Where Quiet Rivers Meet"

Target Market(s)

Collegiate Musician, Professional Musicians, Music Faculty

Industry/Entity Type

Advertising

Requirements
Must have
• 1. Title of the Concert: "Where Quiet Rivers Meet"
2. "Larkmoor Saxophone Quartet Presents"
3. Date (April 23)
4. Time: 5pm
5. Location: Chapel of The Blessed Orrin
Nice to have
• Nice to maybe keep the idea of "Montana" and that mountian-esque feel

```html
<!DOCTYPE html>
<html lang="en">
<head>
<meta charset="utf-8">
<title>Larkmoor Saxophone Quartet — Where Quiet Rivers Meet</title>
<link rel="stylesheet" href="https://fonts.googleapis.com/css2?family=Josefin+Sans:wght@600;700&family=Great+Vibes&display=swap">
<style>
  :root {
    --sky-top: #8cc0ee;
    --sky-mid: #a9c6ea;
    --sky-haze: #c3b6d8;
    --ridge: #8a4a78;
    --ridge-dark: #5b2f55;
    --valley: #3a2538;
    --night: #1d1a20;
    --ink-blue: #4d7cae;
    --ink-blue-soft: #5d86b3;
    --white: #ffffff;
    --rule-mauve: #a0607a;
    --wave-blue: #8fbfe8;
    --band: rgba(32, 30, 32, 0.82);
    --brass-glow: rgba(196, 150, 78, 0.55);
    --brass-soft: rgba(140, 100, 50, 0.35);
  }
  * { margin: 0; padding: 0; box-sizing: border-box; }
  html, body { width: 776px; height: 1200px; overflow: hidden; background: var(--night); }
  .poster {
    position: relative;
    width: 776px;
    height: 1200px;
    overflow: hidden;
    font-family: "Josefin Sans", sans-serif;
    color: var(--white);
    text-transform: uppercase;
  }
  .landscape {
    position: absolute; inset: 0;
    background: linear-gradient(180deg,
      var(--sky-top) 0%,
      var(--sky-mid) 22%,
      var(--sky-haze) 36%,
      #b98bb0 40%,
      var(--ridge) 44%,
      var(--ridge-dark) 52%,
      var(--valley) 60%,
      #2a2230 70%,
      var(--night) 100%);
  }
  .instrument-photo {
    position: absolute; left: 0; top: 780px; width: 776px; height: 420px;
    background:
      radial-gradient(ellipse 260px 120px at 640px 140px, var(--brass-glow), transparent 70%),
      radial-gradient(ellipse 240px 200px at 180px 200px, var(--brass-glow), transparent 70%),
      radial-gradient(ellipse 420px 160px at 380px 240px, var(--brass-soft), transparent 75%);
  }
  .center { position: absolute; left: 0; width: 100%; text-align: center; }
  .ensemble {
    top: 50px; font-size: 29px; font-weight: 700;
    letter-spacing: 2.5px; color: var(--ink-blue);
  }
  .presents {
    top: 114px; font-size: 17px; font-weight: 600;
    letter-spacing: 1.5px; color: var(--ink-blue-soft);
  }
  .wave { position: absolute; left: 50%; transform: translateX(-50%); }
  .concert-title {
    position: absolute; left: 10px; top: 250px; width: 756px;
    font-family: "Great Vibes", cursive;
    font-weight: 400;
    text-transform: none;
    font-size: 124px; line-height: 116px;
    text-align: center;
    transform: rotate(-15deg);
    text-shadow: 0 2px 6px rgba(40, 40, 80, 0.25);
  }
  .concert-title .line-two { display: block; padding-left: 110px; }
  .concert-title .line-one { display: block; padding-right: 40px; }
  .featuring { top: 604px; font-size: 16px; font-weight: 600; letter-spacing: 1.5px; }
  .composer { top: 636px; font-size: 46px; font-weight: 700; letter-spacing: 3px; }
  .performing-row {
    position: absolute; top: 697px; left: 0; width: 100%;
    display: flex; justify-content: center; align-items: center; gap: 22px;
    font-size: 17px; font-weight: 600; letter-spacing: 1.5px;
  }
  .works {
    position: absolute; top: 744px; left: 0; width: 100%;
    display: flex; justify-content: center; gap: 36px;
    font-size: 17px; font-weight: 600; letter-spacing: 1px;
    list-style: none;
  }
  .work { display: flex; align-items: flex-end; gap: 10px; }
  .details-band {
    position: absolute; left: 0; top: 1006px; width: 100%; height: 134px;
    background: var(--band);
  }
  .date { top: 1036px; font-size: 37px; font-weight: 700; letter-spacing: 3px; }
  .venue { top: 1090px; font-size: 23px; font-weight: 600; letter-spacing: 2.5px; }
</style>
</head>
<body>
<main class="poster">
  <div class="landscape" role="img" aria-label="Photograph of a Montana valley at dusk with rose-lit mountain ridges under a pale blue sky"></div>
  <div class="instrument-photo" role="img" aria-label="Photograph of a brass tenor saxophone lying diagonally across the lower poster"></div>

  <p class="center ensemble">Larkmoor Saxophone Quartet</p>
  <p class="center presents">Presents</p>
  <svg class="wave" style="top:150px" width="44" height="10" viewBox="0 0 44 10" aria-hidden="true">
    <path d="M2 7 Q7 1 12 7 T22 7 T32 7 T42 7" fill="none" stroke="var(--white)" stroke-width="2"/>
  </svg>

  <h1 class="concert-title"><span class="line-one">“Where Quiet</span><span class="line-two">Rivers Meet”</span></h1>

  <p class="center featuring">Featuring</p>
  <p class="center composer">Peter Oskivar</p>

  <div class="performing-row">
    <svg width="90" height="8" viewBox="0 0 90 8" aria-hidden="true">
      <path d="M0 5 Q3 1 6 5 T12 5 T18 5 T24 5 T30 5 T36 5 T42 5 T48 5 T54 5 T60 5 T66 5 T72 5 T78 5 T84 5 T90 5" fill="none" stroke="var(--rule-mauve)" stroke-width="1.5"/>
    </svg>
    <span>Performing</span>
    <svg width="90" height="8" viewBox="0 0 90 8" aria-hidden="true">
      <path d="M0 5 Q3 1 6 5 T12 5 T18 5 T24 5 T30 5 T36 5 T42 5 T48 5 T54 5 T60 5 T66 5 T72 5 T78 5 T84 5 T90 5" fill="none" stroke="var(--rule-mauve)" stroke-width="1.5"/>
    </svg>
  </div>

  <ul class="works">
    <li class="work">
      <svg width="18" height="28" viewBox="0 0 18 28" aria-hidden="true"><ellipse cx="6" cy="23" rx="5.5" ry="4" fill="var(--white)"/><path d="M11 23 V2 Q13 8 17 11" fill="none" stroke="var(--white)" stroke-width="2"/></svg>
      <span>Harbor Lanterns</span>
    </li>
    <li class="work">
      <svg width="18" height="28" viewBox="0 0 18 28" aria-hidden="true"><ellipse cx="6" cy="23" rx="5.5" ry="4" fill="var(--white)"/><path d="M11 23 V2 Q13 8 17 11" fill="none" stroke="var(--white)" stroke-width="2"/></svg>
      <span>Vesper Ledger</span>
    </li>
  </ul>

  <div class="details-band"></div>
  <svg class="wave" style="top:996px" width="140" height="10" viewBox="0 0 140 10" aria-hidden="true">
    <path d="M0 6 Q3.5 1 7 6 T14 6 T21 6 T28 6 T35 6 T42 6 T49 6 T56 6 T63 6 T70 6 T77 6 T84 6 T91 6 T98 6 T105 6 T112 6 T119 6 T126 6 T133 6 T140 6" fill="none" stroke="var(--wave-blue)" stroke-width="2"/>
  </svg>
  <p class="center date">Tuesday, April 23 at 5pm</p>
  <p class="center venue">Chapel of the Blessed Orrin</p>
  <svg class="wave" style="top:1140px" width="140" height="10" viewBox="0 0 140 10" aria-hidden="true">
    <path d="M0 6 Q3.5 1 7 6 T14 6 T21 6 T28 6 T35 6 T42 6 T49 6 T56 6 T63 6 T70 6 T77 6 T84 6 T91 6 T98 6 T105 6 T112 6 T119 6 T126 6 T133 6 T140 6" fill="none" stroke="var(--wave-blue)" stroke-width="2"/>
  </svg>
</main>
</body>
</html>
```